Tolvane Facebook page

Provide a facebook page for a business that is an online farmstand for mostly organic farm products produced on our 9 farms and packaged at our mill. We will be targeting an urban and suburban audience that will be able know the farms where their food is grown and "pick" their food online. We want the site to feel to feel fresh and urbane. Winning logo attached.
Currently contest running for website - See more functionality detail there.
Reason: Launched project late.
Reason: Incorrect project start posted. Should end after website contest.
Urbane women who want to know where their food is coming from.
Farm

```html
<!DOCTYPE html>
<html lang="en">
<head>
<meta charset="utf-8">
<title>Tolvane – Page</title>
<link rel="stylesheet" href="https://fonts.googleapis.com/css2?family=Montserrat:wght@600;700&family=PT+Sans:wght@400;700&display=swap">
<style>
  :root {
    --bg: #e9ebf1;
    --bar: #6d84b4;
    --bar-edge: #5b6fa0;
    --card: #ffffff;
    --card-edge: #d3d8e2;
    --link: #3b5998;
    --ink: #1c2a47;
    --muted: #8a94a8;
    --faint: #b8c0cf;
    --green-dark: #2f7a0c;
    --green: #5fc112;
    --green-light: #a6e05a;
    --panel-ink: #2f3a2a;
    --tab-grey: #eff1f6;
  }
  * { margin: 0; padding: 0; box-sizing: border-box; }
  html, body { width: 1200px; height: 639px; overflow: hidden; }
  body {
    position: relative;
    background: var(--bg);
    font-family: "PT Sans", Tahoma, sans-serif;
    color: var(--ink);
  }
  .abs { position: absolute; }

  .top-bar { left: 0; top: 0; width: 1200px; height: 24px; background: var(--bar); border-bottom: 1px solid var(--bar-edge); }
  .side-ghost { left: 36px; top: 285px; width: 99px; height: 140px; border: 1px solid #eef0f5; }

  /* Main header card */
  .header-card { left: 215px; top: 26px; width: 764px; height: 450px; background: var(--card); border: 1px solid var(--card-edge); border-radius: 2px; }
  .cover { left: 215px; top: 26px; width: 764px; height: 284px;
    background: radial-gradient(ellipse at 40% 55%, var(--green-light) 0%, var(--green) 35%, var(--green-dark) 80%, #1f4d10 100%); }

  .brand-panel { left: 239px; top: 26px; width: 143px; height: 338px;
    background: linear-gradient(180deg, rgba(222,240,205,.82), rgba(205,236,170,.78));
    text-align: center; font-family: "Montserrat", Arial, sans-serif; font-weight: 700; color: var(--panel-ink);
    letter-spacing: 1px; }
  .brand-panel .farms { position: absolute; top: 34px; width: 100%; font-size: 15px; }
  .brand-panel .pick { position: absolute; top: 74px; width: 100%; font-size: 15px; line-height: 20px; }
  .brand-panel .mark { position: absolute; top: 248px; left: 60px; width: 22px; height: 22px; border-radius: 50%; background: var(--panel-ink); }
  .brand-panel .name { position: absolute; top: 282px; width: 100%; font-size: 17px; letter-spacing: 1.5px; }
  .profile-frame { left: 235px; top: 305px; width: 154px; height: 63px; border: 1px solid #c3c9d5; border-top: none; box-shadow: 0 1px 2px rgba(0,0,0,.15); }

  .page-name { left: 401px; top: 321px; font-size: 19px; font-weight: 700; color: var(--ink); }
  .like-count { left: 401px; top: 346px; font-size: 10px; color: var(--muted); }

  .btn { border: 1px solid #9aa4b8; border-radius: 2px; background: linear-gradient(#fafbfc, #e6e9ef); font-size: 12px; font-weight: 700; color: #333; display: flex; align-items: center; justify-content: center; gap: 4px; }
  .btn-liked { left: 851px; top: 324px; width: 58px; height: 22px; }
  .btn-gear { left: 918px; top: 324px; width: 39px; height: 22px; }

  .tab-row { top: 378px; height: 66px; }
  .tab-about { left: 216px; width: 293px; background: var(--tab-grey); border-top: 1px solid #e2e5ec; border-bottom: 1px solid #e2e5ec; }
  .tab-about .info { position: absolute; left: 24px; top: 17px; width: 32px; height: 32px; border-radius: 50%; background: #dfe3ec; border: 1px solid #c6ccd9; color: #9aa3b6; font-weight: 700; font-size: 18px; text-align: center; line-height: 30px; font-family: Georgia, serif; }
  .tab-tile { width: 100px; background: linear-gradient(135deg, var(--green-light), var(--green) 55%, var(--green-dark)); color: #fff; font-family: "Montserrat", Arial, sans-serif; font-weight: 700; font-size: 15px; letter-spacing: 1px; line-height: 19px; display: flex; align-items: center; justify-content: center; text-align: center; }
  .tab-more { left: 945px; width: 33px; background: var(--tab-grey); border: 1px solid #e2e5ec; border-right: none; }
  .tab-label { top: 451px; font-size: 10px; color: var(--link); }

  .timeline-spine { left: 596px; top: 476px; width: 2px; height: 163px; background: #c9d0dc; }
  .highlights { left: 564px; top: 493px; width: 68px; height: 20px; background: #f2f3f6; border: 1px solid #ccd2dd; border-radius: 2px; font-size: 10px; color: var(--muted); display: flex; align-items: center; justify-content: center; gap: 4px; }

  .composer { left: 216px; top: 539px; width: 368px; height: 68px; background: var(--card); border: 1px solid var(--card-edge); }
  .composer .option { position: absolute; top: 13px; font-size: 11px; font-weight: 700; color: var(--link); display: flex; align-items: center; gap: 5px; }
  .composer .option.active { color: var(--ink); }
  .composer .sep { position: absolute; top: 5px; width: 1px; height: 30px; background: #e3e6ec; }
  .composer .input { position: absolute; left: 5px; top: 36px; width: 356px; height: 26px; border: 1px solid #bdc7d8; font-size: 11px; color: #777; padding: 5px 5px; }
  .icon { width: 12px; height: 12px; border-radius: 1px; }

  .friends-card { left: 610px; top: 539px; width: 368px; height: 110px; background: var(--card); border: 1px solid var(--card-edge); }
  .friends-card .count { position: absolute; left: 14px; top: 12px; font-size: 25px; font-weight: 700; color: var(--link); }
  .friends-card .title { position: absolute; left: 35px; top: 15px; font-size: 11px; font-weight: 700; color: var(--link); }
  .friends-card .sub { position: absolute; left: 35px; top: 28px; font-size: 10px; color: var(--muted); }
  .friends-card .rule { position: absolute; left: 14px; top: 48px; width: 340px; height: 1px; background: #e5e8ee; }
  .avatar { position: absolute; top: 52px; width: 33px; height: 32px; }

  /* Right column */
  .create-page { left: 991px; top: 36px; width: 74px; height: 19px; background: var(--link); border: 1px solid #29447e; border-radius: 2px; color: #fff; font-size: 11px; font-weight: 700; text-align: center; line-height: 17px; }
  .right-rule { left: 990px; height: 1px; background: #d6dbe5; }
  .time-nav { left: 990px; font-size: 10px; color: var(--faint); border-left: 3px solid #d6dbe5; padding-left: 8px; height: 18px; line-height: 18px; }
  .time-nav.current { color: var(--link); font-weight: 700; border-left-color: var(--link); }

  .ad-head { left: 990px; top: 488px; font-size: 11px; font-weight: 700; color: #555; }
  .ad-title { left: 990px; top: 508px; font-size: 11px; font-weight: 700; color: var(--link); }
  .ad-image { left: 990px; top: 525px; width: 90px; height: 67px; background: linear-gradient(180deg, #e9eef6, #b9c6da); display: flex; align-items: center; justify-content: center; }
  .ad-image span { font-family: "PT Sans", Tahoma, sans-serif; font-weight: 700; font-size: 12px; color: #2d4a34; }
  .ad-like { left: 990px; top: 597px; font-size: 10px; color: #666; display: flex; gap: 3px; align-items: center; }
  .ad-like b { color: var(--link); font-weight: 400; }
  .advertise { left: 991px; top: 616px; width: 115px; height: 19px; border: 1px solid #999; background: #f5f6f7; font-size: 11px; font-weight: 700; color: #333; text-align: center; line-height: 17px; }
</style>
</head>
<body>
  <div class="abs top-bar"></div>
  <div class="abs side-ghost"></div>

  <div class="abs header-card"></div>
  <div class="abs cover" role="img" aria-label="Close-up photo of a bright green apple splashed with water droplets"></div>

  <div class="abs brand-panel">
    <div class="farms">9 FARMS</div>
    <div class="pick">PICK YOUR<br>OWN FOOD</div>
    <div class="mark"></div>
    <div class="name">TOLVANE</div>
  </div>
  <div class="abs profile-frame"></div>

  <div class="abs page-name">Fenwick test2</div>
  <div class="abs like-count">13 likes</div>

  <div class="abs btn btn-liked">
    <svg width="9" height="8" viewBox="0 0 9 8"><path d="M1 4 L3.5 6.5 L8 1" stroke="#555" stroke-width="1.6" fill="none"/></svg>Liked
  </div>
  <div class="abs btn btn-gear">
    <svg width="10" height="10" viewBox="0 0 10 10"><circle cx="5" cy="5" r="3.2" fill="none" stroke="#555" stroke-width="1.6" stroke-dasharray="1.6 0.9"/><circle cx="5" cy="5" r="1" fill="#555"/></svg>
    <svg width="8" height="5" viewBox="0 0 8 5"><path d="M0 0 H8 L4 5Z" fill="#6d84b4"/></svg>
  </div>

  <div class="abs tab-row tab-about"><div class="info">i</div></div>
  <div class="abs tab-row tab-tile" style="left:517px" role="img" aria-label="Green apple photo tile"></div>
  <div class="abs tab-row tab-tile" style="left:623px">WWW</div>
  <div class="abs tab-row tab-tile" style="left:731px">NEWS<br>LETTER</div>
  <div class="abs tab-row tab-tile" style="left:837px">CONTACT</div>
  <div class="abs tab-row tab-more"></div>

  <div class="abs tab-label" style="left:254px">About</div>
  <div class="abs tab-label" style="left:516px">Photos</div>
  <div class="abs tab-label" style="left:623px">Photos</div>
  <div class="abs tab-label" style="left:731px">About Me</div>
  <div class="abs tab-label" style="left:837px">3pages</div>

  <div class="abs timeline-spine"></div>
  <div class="abs highlights">Highlights
    <svg width="7" height="4" viewBox="0 0 7 4"><path d="M0 0 H7 L3.5 4Z" fill="#9aa3b6"/></svg>
  </div>

  <div class="abs composer">
    <div class="option active" style="left:16px"><span class="icon" style="background:#f3d27a;border:1px solid #c9a54a"></span>Status</div>
    <div class="sep" style="left:74px"></div>
    <div class="option" style="left:93px"><span class="icon" style="background:#d8b27c;border:1px solid #8a6a3c"></span>Photo / Video</div>
    <div class="sep" style="left:188px"></div>
    <div class="option" style="left:206px"><span class="icon" style="background:#fff;border:1px solid #b33;border-top:3px solid #c33"></span>Event, Milestone +</div>
    <div class="input">Write something...</div>
  </div>

  <div class="abs friends-card">
    <div class="count">6</div>
    <div class="title">Friends</div>
    <div class="sub">Like Fenwick test2</div>
    <div class="rule"></div>
    <div class="avatar" style="left:14px;background:#2f3a4a" role="img" aria-label="Friend profile photo"></div>
    <div class="avatar" style="left:48px;background:#4c5a44" role="img" aria-label="Friend profile photo"></div>
    <div class="avatar" style="left:82px;background:#9a7a5e" role="img" aria-label="Friend profile photo"></div>
    <div class="avatar" style="left:116px;background:#7f93b0" role="img" aria-label="Friend profile photo"></div>
    <div class="avatar" style="left:150px;background:#b9c7dc" role="img" aria-label="Friend profile photo"></div>
    <div class="avatar" style="left:184px;background:#b5624a" role="img" aria-label="Friend profile photo"></div>
  </div>

  <div class="abs create-page">Create Page</div>
  <div class="abs right-rule" style="top:66px;width:210px"></div>
  <div class="abs time-nav current" style="top:76px">Now</div>
  <div class="abs time-nav" style="top:97px">October</div>
  <div class="abs time-nav" style="top:118px">Born</div>

  <div class="abs ad-head">See Your Ad Here</div>
  <div class="abs right-rule" style="top:504px;width:210px"></div>
  <div class="abs ad-title">Fenwick test2</div>
  <div class="abs ad-image" role="img" aria-label="Advert image with sky background"><span>stallkeep</span></div>
  <div class="abs ad-like">
    <svg width="10" height="10" viewBox="0 0 10 10"><path d="M1 4 H3 V9 H1Z M4 4 L6 0.5 Q7 1 6.5 3.5 H9 V7 L7.5 9 H4Z" fill="#6d84b4"/></svg>
    <b>Like</b> · Marek Dunst likes this.
  </div>
  <div class="abs advertise">Advertise Your Page</div>
</body>
</html>
```